BriskwayLane.com needs updated website design.

BriskwayLane.com offers individuals a quick, hassle-free way of selling their car, rv, or boat in the Sun City Center, FL area. We will come to the customer's place of choosing in order to give them an in-person offer for their car, rv, or boat. Looking for a website design that will allow users to input their vehicle details as well as their contact info in order to schedule a time and place for our staff to come make them an offer. Currently have an active site that can be referenced.

Target Market(s)

Older people who no longer need their cars.

Industry/Entity Type

Automotive

Coding

Coded - Design and coding required

Number of Pages Required

3 page

Font styles to use
Sans Serif

Colors
a1cd3a
33b8a4

Requirements
Must have
• Trustworthy theme, Emphasis on capturing contact info (contact form visible at all times). Standard privacy policy. Wordpress theme

```html
<!DOCTYPE html>
<html lang="en">
<head>
<meta charset="utf-8">
<title>BriskwayLane.com – Sell Your Car Today</title>
<link rel="stylesheet" href="https://fonts.googleapis.com/css2?family=Poppins:ital,wght@0,400;0,500;0,600;0,700;0,800;1,500;1,600&display=swap">
<style>
:root{
  --lime:#a1cd3a;
  --teal:#33b8a4;
  --ink:#1b1f24;
  --text:#555b61;
  --muted:#8a8f94;
  --soft:#f5f5f5;
  --field:#f3f4f4;
  --navy:#0d2f4f;
  --footer:#0a1624;
  --white:#fff;
}
*{box-sizing:border-box;margin:0;padding:0}
html,body{width:1200px;height:3141px;overflow:hidden}
body{font-family:"Poppins",sans-serif;color:var(--text);background:var(--white);position:relative}
section,header,footer,div{position:relative}

/* top bar */
.topbar{height:37px;background:var(--lime);color:var(--white);font-size:10.5px;font-weight:500}
.topbar .contact{position:absolute;left:225px;top:12px;word-spacing:1px}
.topbar .social{position:absolute;right:225px;top:8px;display:flex;gap:7px}
.topbar .social span{width:21px;height:21px;background:var(--white);border-radius:3px;display:block;opacity:.95}

/* header */
.site-header{height:75px;background:var(--white)}
.brand{position:absolute;left:226px;top:14px;display:flex;align-items:center;gap:10px}
.brand .dot{width:40px;height:40px;border-radius:50%;background:var(--teal)}
.brand .name{font-size:21px;font-weight:700;color:var(--ink);line-height:1}
.brand .tag{font-size:9px;font-weight:600;color:var(--lime);margin-top:4px}
.nav{position:absolute;left:591px;top:31px;display:flex;gap:32px;font-size:10.5px;font-weight:500;color:var(--ink)}
.btn{display:inline-flex;align-items:center;gap:10px;border:2px solid var(--teal);background:var(--teal);color:var(--white);border-radius:20px;font-weight:600;padding:0 20px 0 4px;height:31px;font-size:13px}
.btn .dot{width:22px;height:22px;border-radius:50%;background:var(--white)}
.header-btn{position:absolute;left:837px;top:22px}

/* hero */
.hero{height:482px;background:linear-gradient(100deg,#2d7f82 0%,#3aa099 35%,#2f8d8c 60%,#4aa9a2 100%)}
.hero-copy{position:absolute;left:225px;top:156px;width:370px;color:var(--white)}
.hero-copy h1{font-size:31px;font-weight:700;line-height:1.22}
.hero-copy .quote{font-style:italic;font-weight:600;font-size:13px;margin-top:17px}
.hero-copy p{font-size:11px;line-height:1.7;margin-top:12px;font-weight:500}
.quote-form{position:absolute;left:654px;top:54px;width:322px;height:374px;background:var(--white);padding:20px 19px}
.quote-form h2{text-align:center;font-size:19px;font-weight:600;color:var(--ink);margin-bottom:17px}
.row{display:flex;gap:11px;margin-bottom:11px}
.field{flex:1;height:30px;background:var(--field);font-size:8.5px;color:#555;display:flex;align-items:center;padding:0 10px;justify-content:space-between}
.field.chev::after{content:"";width:5px;height:5px;border-right:1px solid #555;border-bottom:1px solid #555;transform:rotate(45deg);margin-top:-3px}
.field.full{height:30px;margin-bottom:12px}
.quote-form .btn{position:absolute;left:92px;top:327px;height:30px;font-size:12.5px}

/* features */
.features{height:223px}
.feature{position:absolute;top:49px;width:200px;text-align:center;margin-left:-100px}
.feature .icon{width:62px;height:62px;margin:0 auto;background:var(--white);box-shadow:0 2px 8px rgba(0,0,0,.1);display:flex;align-items:center;justify-content:center}
.feature h3{color:var(--teal);font-size:13px;font-weight:600;margin-top:26px}
.feature p{font-size:10px;margin-top:6px;color:var(--text)}
.connector{position:absolute;top:72px;height:1px;border-top:1px dashed #cfd8d6}

/* vehicles */
.vehicles{height:521px;background:var(--soft)}
.card{position:absolute;top:51px;width:344px;height:344px;overflow:hidden}
.card .label{position:absolute;left:0;right:0;bottom:22px;text-align:center;font-size:60px;font-weight:800;color:var(--white);letter-spacing:1px}
.card.car{left:62px;background:linear-gradient(180deg,#6f8d3e 0%,#c3a930 55%,#4b4b45 100%)}
.card.rv{left:428px;background:linear-gradient(180deg,#9da3a8 0%,#d8d6cf 50%,#5d6466 100%)}
.card.boat{left:794px;background:linear-gradient(180deg,#2a6ea0 0%,#6aa2c4 50%,#1f5a86 100%)}
.vehicles .btn{position:absolute;left:502px;top:439px;height:31px}

/* about + testimonials */
.story{height:651px;background:linear-gradient(170deg,#1c4666 0%,#15406a 40%,#0f3558 100%);color:var(--white)}
.about{position:absolute;left:225px;top:60px;width:370px}
.about h2{color:var(--lime);font-size:19px;font-weight:600}
.about p{font-size:10.2px;line-height:1.85;font-weight:500;margin-top:15px}
.about ul{list-style:none;margin-top:15px}
.about li{font-size:10px;font-style:italic;line-height:1.75;padding-left:11px;position:relative;margin-bottom:9px}
.about li::before{content:"";position:absolute;left:0;top:7px;width:5px;height:5px;border-radius:50%;background:var(--lime)}
.testimonials h2{position:absolute;left:0;right:0;top:396px;text-align:center;font-size:19px;font-weight:600}
.review{position:absolute;top:452px;width:345px}
.review .who{display:flex;align-items:center;gap:13px}
.review .avatar{width:44px;height:44px;border-radius:50%;background:#dfe5ea;border:2px solid var(--white)}
.review h4{font-size:14px;font-weight:600}
.review .stars{color:var(--teal);font-size:10px;letter-spacing:1px}
.review .stars span{color:var(--white)}
.review p{font-size:10.2px;line-height:1.82;margin-top:16px;font-weight:500}

/* gallery split */
.gallery{height:374px;background:var(--white)}
.gallery .left{position:absolute;left:0;top:0;width:597px;height:374px;background:linear-gradient(180deg,#4d87bf 0%,#cfdbe6 55%,#2f5d7a 100%)}
.gallery .right{position:absolute;left:604px;top:0;width:596px;height:374px;background:linear-gradient(180deg,#8a9a9c 0%,#d9d6ce 50%,#6a6459 100%)}
.gallery .badge{position:absolute;left:551px;top:139px;width:98px;height:98px;border-radius:50%;background:var(--white);display:flex;align-items:center;justify-content:center}
.gallery .badge span{width:64px;height:64px;border-radius:50%;background:var(--teal)}

/* faq */
.faq{height:430px}
.faq h2{position:absolute;left:0;right:0;top:50px;text-align:center;font-size:19px;font-weight:600;color:var(--ink)}
.faq-item{position:absolute;left:225px;width:750px;border:1px solid #e4e6e6;background:var(--white);font-size:11px;font-weight:600;color:var(--ink);padding:11px 13px}
.faq-item .sign{position:absolute;right:12px;top:8px;font-weight:400;font-size:15px;color:#444}
.faq-item .answer{font-size:8.6px;font-weight:400;color:var(--muted);line-height:18.5px;margin-top:5px}

/* footer */
.site-footer{height:348px;background:var(--footer);color:#cfd4d9}
.f-brand{position:absolute;left:225px;top:50px;display:flex;align-items:center;gap:8px}
.f-brand .dot{width:30px;height:30px;border-radius:50%;background:var(--teal)}
.f-brand .name{font-size:14px;font-weight:700;color:var(--white);line-height:1}
.f-brand .tag{font-size:6.5px;color:var(--lime);font-weight:600;margin-top:2px}
.f-about{position:absolute;left:225px;top:112px;width:260px;font-size:9.2px;line-height:2}
.f-social{position:absolute;left:225px;top:236px;display:flex;gap:9px}
.f-social span{width:30px;height:30px;border-radius:50%;background:var(--white)}
.f-social span:first-child{background:var(--teal)}
.f-col{position:absolute;top:62px}
.f-col h5{color:var(--white);font-size:12.5px;font-weight:600;margin-bottom:18px}
.f-col a{display:block;color:#cfd4d9;text-decoration:none;font-size:9px;margin-bottom:19px}
.f-col .k{font-size:9px;font-weight:600;color:var(--white)}
.f-col .v{font-size:9px;line-height:1.9;margin-bottom:12px}
.f-rule{position:absolute;left:225px;width:750px;top:300px;border-top:1px solid #24303d}
.copyright{position:absolute;left:0;right:0;top:323px;text-align:center;font-size:8.5px;color:#aab1b8}
</style>
</head>
<body>

<div class="topbar">
  <div class="contact">Call Us : 555-014-2290 &nbsp;&nbsp;&nbsp;&nbsp;| &nbsp;&nbsp;&nbsp;&nbsp;Email : hello@briskwaylane.com</div>
  <div class="social" aria-label="Social links"><span></span><span></span><span></span><span></span></div>
</div>

<header class="site-header">
  <div class="brand"><span class="dot"></span><div><div class="name">BriskwayLane.com</div><div class="tag">Sell your Car Today</div></div></div>
  <nav class="nav"><span>HOME</span><span>ABOUT US</span><span>CONTACT US</span></nav>
  <span class="btn header-btn"><span class="dot"></span>Contact Us</span>
</header>

<section class="hero" role="img" aria-label="Teal-toned photo of a sports car interior and front">
  <div class="hero-copy">
    <h1>Get Your Free In Person Cash Offer Today</h1>
    <div class="quote">"Don't Sell Til You Give Me A Yell"</div>
    <p>Lorem ipsum dolor sit amet, consectetur adipiscing elit, sed do eiusmod tempor incididunt ut labore et dolore magna aliqua. Ut enim ad minim veniam,</p>
  </div>
  <form class="quote-form">
    <h2>Get your Car Price</h2>
    <div class="row"><div class="field chev">Select Year</div><div class="field chev">Select Brand</div></div>
    <div class="row"><div class="field chev">Select Model</div><div class="field chev">Select Variant</div></div>
    <div class="row" style="margin-bottom:12px"><div class="field chev">Select City</div><div class="field">Kilometers Driven</div></div>
    <div class="field full">Full Name</div>
    <div class="field full">Email Address</div>
    <div class="field full">Mobile Number</div>
    <span class="btn"><span class="dot"></span>Submit Now</span>
  </form>
</section>

<section class="features">
  <div class="connector" style="left:344px;width:128px"></div>
  <div class="connector" style="left:536px;width:127px"></div>
  <div class="connector" style="left:727px;width:129px"></div>
  <div class="feature" style="left:312px">
    <div class="icon"><svg width="40" height="40" viewBox="0 0 40 40" fill="none" stroke="#222" stroke-width="1.6"><circle cx="22" cy="22" r="12"/><circle cx="22" cy="22" r="8" stroke="#33b8a4"/><path d="M22 22l4-4M20 7h4M22 7v3M4 18h7M6 23h5M4 28h7"/></svg></div>
    <h3>FAST</h3><p>I'll Be at Your Door Today</p>
  </div>
  <div class="feature" style="left:504px">
    <div class="icon"><svg width="40" height="40" viewBox="0 0 40 40" fill="none" stroke="#222" stroke-width="1.6"><path d="M20 6v20M10 10h20M10 10l-5 9h10zM30 10l-5 9h10z"/><path d="M6 26c4 6 8 8 14 8s10-2 14-8" stroke="#33b8a4"/></svg></div>
    <h3>FAIR</h3><p>Get Fair Price for Your Vehicle</p>
  </div>
  <div class="feature" style="left:695px">
    <div class="icon"><svg width="40" height="40" viewBox="0 0 40 40" fill="none" stroke="#222" stroke-width="1.6"><path d="M6 30l8-8 6 4 6-4 8 8"/><path d="M14 22l6-10 6 10" stroke="#33b8a4"/><circle cx="20" cy="9" r="3"/></svg></div>
    <h3>FRIENDLY</h3><p>Trusted for Over 25 Years</p>
  </div>
  <div class="feature" style="left:888px">
    <div class="icon"><svg width="40" height="40" viewBox="0 0 40 40" fill="none" stroke="#222" stroke-width="1.6"><path d="M14 34V16l6-8 4 3-3 6h9v10l-4 7z"/><path d="M18 22l3 3 5-6" stroke="#33b8a4"/></svg></div>
    <h3>HASSLE FREE</h3><p>I Handle All the Paperwork</p>
  </div>
</section>

<section class="vehicles">
  <div class="card car" role="img" aria-label="Photo of a yellow sports car parked under trees"><div class="label">CAR</div></div>
  <div class="card rv" role="img" aria-label="Photo of a camper van parked by a lake at sunset"><div class="label">RV VAN</div></div>
  <div class="card boat" role="img" aria-label="Photo of a speedboat cruising on blue water"><div class="label">BOAT</div></div>
  <span class="btn"><span class="dot"></span>Schedule for Meeting</span>
</section>

<section class="story" role="img" aria-label="Dark blue photo of a speedboat carving a wake across the sea">
  <div class="about">
    <h2>About Us</h2>
    <p>We offer the most convenient way of selling your vehicle. We will come to you at a place of your choosing, i.e. home, office, or any other public place. &nbsp;We will give you an in person cash offer on the spot.</p>
    <ul>
      <li>Got an old clunker? I'll Buy It! – Turn it into cash today!</li>
      <li>Got a nice car you just don't need? I'll Buy It! – Stop wasting money on insurance, registration and maintenance costs!</li>
      <li>Got a car that needs repairs? I'll Buy It! – No matter what the issue is I'll come take it away today!</li>
    </ul>
  </div>
  <div class="testimonials">
    <h2>Customer Testimonial</h2>
    <div class="review" style="left:225px">
      <div class="who"><span class="avatar" role="img" aria-label="Customer portrait"></span><div><h4>Dorian Keller</h4><div class="stars">★★★★<span>★</span></div></div></div>
      <p>Lorem ipsum dolor sit amet, consectetur adipiscing elit, sed do eiusmod tempor incididunt ut labore et dolore magna aliqua. Ut enim ad minim veniam, quis nostrud exercitation ullamco laboris nisi ut aliquip ex ea commodo consequat. Duis aute irure dolor in reprehenderit in voluptate velit esse cillum dolore eu fugiat.</p>
    </div>
    <div class="review" style="left:609px">
      <div class="who"><span class="avatar" role="img" aria-label="Customer portrait"></span><div><h4>Marcus Hale</h4><div class="stars">★★★★<span>★</span></div></div></div>
      <p>Lorem ipsum dolor sit amet, consectetur adipiscing elit, sed do eiusmod tempor incididunt ut labore et dolore magna aliqua. Ut enim ad minim veniam, quis nostrud exercitation ullamco laboris nisi ut aliquip ex ea commodo consequat. Duis aute irure dolor in reprehenderit in voluptate velit esse cillum dolore eu fugiat.</p>
    </div>
  </div>
</section>

<section class="gallery">
  <div class="left" role="img" aria-label="Photo of a white motor yacht speeding on the water"></div>
  <div class="right" role="img" aria-label="Photo of motorhomes parked near mountain chalets"></div>
  <div class="badge"><span></span></div>
</section>

<section class="faq">
  <h2>Frequently Asked Questions</h2>
  <div class="faq-item" style="top:110px;height:119px">Who is Briskway Lane?<span class="sign">—</span>
    <p class="answer">Lorem ipsum dolor sit amet, consectetur adipiscing elit, sed do eiusmod tempor incididunt ut labore et dolore magna aliqua. Ut enim ad minim veniam, quis nostrud exercitation ullamco laboris nisi ut aliquip ex ea commodo consequat. Duis aute irure dolor in reprehenderit in voluptate velit esse cillum dolore eu fugiat. Lorem ipsum dolor sit amet, consectetur adipiscing elit, sed do eiusmod tempor incididunt ut labore et dolore magna aliqua. Ut enim ad minim veniam, quis nostrud exercitation ullamco laboris nisi ut aliquip ex ea commodo consequat.</p>
  </div>
  <div class="faq-item" style="top:243px;height:36px">Eiusmod tempor incididunt ut labore et dolore?<span class="sign">+</span></div>
  <div class="faq-item" style="top:293px;height:36px">Exercitation Ullamco Laboris Nisi Ut Aliquip?<span class="sign">+</span></div>
  <div class="faq-item" style="top:343px;height:36px">Lorem Ipsum Dolor Sit Amet?<span class="sign">+</span></div>
</section>

<footer class="site-footer">
  <div class="f-brand"><span class="dot"></span><div><div class="name">BriskwayLane.com</div><div class="tag">Sell your Car Today</div></div></div>
  <p class="f-about">Lorem ipsum dolor sit amet, adipisicing elit. Quod corrupti laborum, quasi? Dolor sapiente amet optio harum dolores, voluptate, tempora dolorem fugiat fuga autem. Lorem ipsum dolor sit amet, adipisicing elit. Quod corrupti laborum.</p>
  <div class="f-social" aria-label="Social links"><span></span><span></span><span></span><span></span><span></span></div>
  <div class="f-col" style="left:526px"><h5>Useful Links</h5><a>About Us</a><a>- Services</a><a>Blog</a><a>FAQs</a><a>Contact Us</a></div>
  <div class="f-col" style="left:682px"><h5>Other Links</h5><a>Support</a><a>Privacy Policy</a><a>Terms &amp; Conditions</a><a>Sitemap</a></div>
  <div class="f-col" style="left:821px"><h5>Contact Us</h5>
    <div class="k">Address:-</div><div class="v">48 Palmetto Row, Lakeview,<br>FL 30000, USA.</div>
    <div class="k">Mobile:-</div><div class="v">555-014-2290</div>
    <div class="k">Email Address:-</div><div class="v">hello@briskwaylane.com</div>
  </div>
  <div class="f-rule"></div>
  <div class="copyright">Copyright © 2020 Briskway Lane. All Rights Reserved</div>
</footer>

</body>
</html>
```